We are an integrated facilities management company.

We aggregate everything related to facilities maintenance. Repair-replacement of equipment and facility space materials from:
Asset gathering and tracking.
Vendor screening, contracting and management.
Service requirement development.
Work order processing and management.
Invoice reconciliation.
Vendor payment.
Reporting.
Capital equipment bids and project management.

Target Market(s)

Retail, hospitality, multi-family housing, long term healthcare.

Industry/Entity Type

Maintenance

Contact Information for Business Card

Professional and bold look. (see logo zip file)

Colors
3377b5
85abd2
cedeed

Requirements
Must have
• N/A
Nice to have
• N/A
Should not have
• N/A

```html
<!DOCTYPE html>
<html lang="en">
<head>
<meta charset="utf-8">
<title>Northgate Facility Services – Business Card</title>
<link href="https://fonts.googleapis.com/css2?family=PT+Sans:wght@400;700&display=swap" rel="stylesheet">
<style>
  :root {
    --brand-blue: #336190;
    --brand-blue-light: #85abd2;
    --brand-blue-pale: #cedeed;
    --slate: #3d4a55;
    --paper: #f7f8f9;
    --ink: #2f3438;
    --backdrop: #e4e6e8;
  }
  * { box-sizing: border-box; margin: 0; padding: 0; }
  html, body {
    width: 1200px; height: 1021px; overflow: hidden;
    background: var(--backdrop);
    font-family: "PT Sans", sans-serif;
  }
  .card {
    position: absolute; left: 250px;
    width: 700px; height: 400px;
    box-shadow: 0 6px 18px rgba(0,0,0,.18);
    overflow: hidden;
  }
  .card-back { top: 70px; background: var(--brand-blue); }
  .card-front { top: 540px; background: var(--paper); }

  .wordmark { position: absolute; display: flex; align-items: center; gap: 14px; }
  .wordmark-square { width: 40px; height: 40px; flex: none; }
  .wordmark-text { font-weight: 700; font-size: 30px; letter-spacing: .5px; text-transform: uppercase; line-height: 1; }
  .tagline { font-size: 13px; letter-spacing: 4px; text-transform: uppercase; margin-top: 6px; }

  .card-back .wordmark { left: 150px; top: 165px; }
  .card-back .wordmark-square { background: #fff; }
  .card-back .wordmark-text, .card-back .tagline { color: #fff; }

  .card-front .wordmark { left: 40px; top: 38px; }
  .card-front .wordmark-square { background: var(--brand-blue); }
  .card-front .wordmark-text { color: var(--brand-blue); font-size: 24px; }
  .card-front .tagline { color: var(--slate); font-size: 11px; letter-spacing: 3px; }

  .contact-panel {
    position: absolute; left: 0; top: 130px;
    width: 430px; height: 170px;
    background: var(--brand-blue); color: #fff;
    padding: 16px 0 0 40px;
  }
  .person-name { font-weight: 700; font-size: 22px; }
  .person-role { font-size: 16px; margin-bottom: 10px; color: var(--brand-blue-pale); }
  .contact-line { display: flex; align-items: center; gap: 10px; font-size: 17px; line-height: 25px; }
  .contact-line svg { width: 14px; height: 14px; flex: none; }

  .address { position: absolute; left: 40px; top: 330px; font-size: 18px; color: var(--ink); }

  .accent-block { position: absolute; right: 0; top: 170px; width: 150px; height: 150px; background: var(--slate); }
  .accent-bar { position: absolute; right: 150px; top: 300px; width: 120px; height: 20px; background: var(--slate); }
</style>
</head>
<body>
  <section class="card card-back">
    <div class="wordmark">
      <span class="wordmark-square"></span>
      <div>
        <div class="wordmark-text">Northgate Facility Services</div>
        <div class="tagline">Maintain • Repair • Replace</div>
      </div>
    </div>
  </section>

  <section class="card card-front">
    <div class="wordmark">
      <span class="wordmark-square"></span>
      <div>
        <div class="wordmark-text">Northgate Facility Services</div>
        <div class="tagline">Maintain • Repair • Replace</div>
      </div>
    </div>

    <div class="contact-panel">
      <div class="person-name">Daniel Reyes</div>
      <div class="person-role">Founder</div>
      <div class="contact-line">
        <svg viewBox="0 0 24 24" fill="#fff"><path d="M6.6 10.8a15.1 15.1 0 0 0 6.6 6.6l2.2-2.2c.3-.3.7-.4 1-.2 1.1.4 2.3.6 3.6.6.6 0 1 .4 1 1V20c0 .6-.4 1-1 1A17 17 0 0 1 3 4c0-.6.4-1 1-1h3.5c.6 0 1 .4 1 1 0 1.3.2 2.5.6 3.6.1.3 0 .7-.2 1z"/></svg>
        <span>(555) 210-4480</span>
      </div>
      <div class="contact-line">
        <svg viewBox="0 0 24 24" fill="none" stroke="#fff" stroke-width="2"><rect x="2" y="5" width="20" height="14"/><path d="M2 5l10 8 10-8"/></svg>
        <span>daniel@northgatefacility.com</span>
      </div>
      <div class="contact-line">
        <svg viewBox="0 0 24 24" fill="none" stroke="#fff" stroke-width="2"><circle cx="12" cy="12" r="10"/><path d="M2 12h20M12 2c3 3 3 17 0 20M12 2c-3 3-3 17 0 20"/></svg>
        <span>www.northgatefacility.com</span>
      </div>
    </div>

    <div class="address">48 Harbor Street, Suite 310, Tampa, Florida, 33602</div>

    <div class="accent-block"></div>
    <div class="accent-bar"></div>
  </section>
</body>
</html>
```